Mediation service showing compassion, collaboration, and resolution

I would like to purchase a customized version of a design you have previously submitted - https://www.pixelbidhub.com/design/48172635

Hello,

I would like a design for a flyer for my mediation business.
I also want to include a message that says that I offer rates on sliding scale.
My website is: www.morvantelkresolve.com

Let me know what other details you might want?

Thank you,

Teodric

Target Market(s)

Local community, western Massachusetts USA. Businesses, families, individuals.

Industry/Entity Type

Mediation, Legal, Alternative Dispute Resolution, Divorce, Unions

Font styles to use
Sans Serif

Colors
0094D4
00A9DD
6FCCEA
C7EBF8
E9F6FB
00AB8E
00BBA5
67D7C9
C6EFE9
E9F9F6

Requirements
Must have
• “Sliding scale rates available “. Phone and email details. +1.555.384.7290 and email: teodric@morvantelkresolve.com as well as we code to my website www.morvantelkresolve.com

```html
<!DOCTYPE html>
<html lang="en">
<head>
<meta charset="utf-8">
<title>Mediation Flyer – Teodric Morvantelk</title>
<link rel="stylesheet" href="https://fonts.googleapis.com/css2?family=Cormorant+Garamond:wght@400;500;600&family=Quicksand:wght@600&display=swap">
<style>
  :root {
    --blue-deep: #0094d4;
    --blue: #00a9dd;
    --blue-soft: #6fccea;
    --blue-pale: #c7ebf8;
    --blue-mist: #e9f6fb;
    --teal: #00bba5;
    --teal-soft: #67d7c9;
    --ink: #1c1c1c;
    --white: #ffffff;
  }
  * { margin: 0; padding: 0; box-sizing: border-box; }
  html, body { width: 982px; height: 1200px; overflow: hidden; background: var(--white); }
  .flyer {
    position: relative; width: 982px; height: 1200px; overflow: hidden;
    background: var(--white);
    font-family: "Cormorant Garamond", Georgia, serif;
    font-weight: 500;
    color: var(--ink);
  }
  .hero-art { position: absolute; left: 0; top: 0; }
  .brand { position: absolute; left: 0; width: 1054px; top: 44px; text-align: center; }
  .brand-name {
    font-weight: 500; font-size: 40px; letter-spacing: 1px; color: var(--ink); line-height: 1;
  }
  .brand-tag {
    margin-top: 12px;
    font-family: "Quicksand", Arial, sans-serif; font-weight: 600;
    font-size: 11.5px; letter-spacing: .4px; color: var(--ink);
  }
  .hero-title {
    position: absolute; left: 40px; top: 270px;
    font-weight: 600; font-size: 68px; letter-spacing: 1px; color: var(--white); line-height: 1;
  }
  .illustration-slot {
    position: absolute; left: 362px; top: 452px; width: 92px; height: 126px;
    background: linear-gradient(160deg, var(--blue-pale), #eef6fb 70%);
    border-radius: 6px;
  }
  .section-head {
    position: absolute; font-size: 28px; font-weight: 500; line-height: 1;
    letter-spacing: .3px; white-space: nowrap; z-index: 1;
  }
  .section-head .accent { color: var(--blue); font-weight: 400; }
  .section-head .strong { color: var(--ink); font-weight: 600; }
  .section-head::after {
    content: ""; position: absolute; left: -4px; right: -8px; bottom: -3px; height: 8px;
    background: var(--blue-mist); z-index: -1;
  }
  .head-what { left: 49px; top: 566px; }
  .head-what::after { right: -100px; }
  .head-services { left: 49px; top: 816px; }
  .head-services .accent { font-weight: 500; }
  .head-services .strong { font-weight: 400; }
  .head-why { left: 553px; top: 455px; }
  .body-copy {
    position: absolute; left: 49px; width: 470px;
    font-size: 16px; line-height: 21.4px;
  }
  .copy-one { top: 604px; }
  .copy-two { top: 710px; }
  .services {
    position: absolute; left: 46px; top: 853px; list-style: none;
    font-size: 16px; line-height: 24.4px; z-index: 1;
  }
  .services li::before {
    content: "\2713"; color: var(--teal); margin-right: 9px; font-family: Arial, sans-serif; font-size: 12px;
  }
  .why-intro {
    position: absolute; left: 553px; top: 493px; width: 290px;
    font-size: 16px; line-height: 21.4px;
  }
  .benefits { position: absolute; left: 550px; top: 553px; list-style: none; width: 370px; }
  .benefit { display: flex; align-items: center; height: 52px; margin-bottom: 20px; }
  .benefit-icon {
    flex: none; width: 54px; height: 52px; border: 1px solid var(--blue-pale);
    background: var(--white); display: flex; align-items: center; justify-content: center;
  }
  .benefit-text { margin-left: 12px; width: 290px; font-size: 16px; line-height: 19.5px; }
  .backdrop-fade { position: absolute; left: 0; top: 780px; }
  .rates-bar {
    position: absolute; left: 366px; top: 1030px; width: 616px; height: 41px;
    background: linear-gradient(90deg, var(--teal-soft), var(--blue-soft) 45%, var(--blue));
    clip-path: polygon(14px 0, 100% 0, 100% 100%, 0 100%);
    color: var(--white); font-size: 19px; font-weight: 500; letter-spacing: .6px;
    padding: 9px 0 0 30px; white-space: nowrap;
  }
  .contact-panel {
    position: absolute; left: 312px; top: 1075px; width: 670px; height: 125px;
    background: linear-gradient(90deg, var(--blue) 10%, var(--blue-soft) 60%, var(--teal-soft));
    clip-path: polygon(48px 0, 100% 0, 100% 100%, 0 100%);
  }
  .panel-edge {
    position: absolute; left: 296px; top: 1075px; width: 58px; height: 125px;
    background: linear-gradient(180deg, var(--blue-pale), var(--blue-soft));
    clip-path: polygon(44px 0, 54px 0, 10px 100%, 0 100%);
  }
  .contact-list {
    position: absolute; left: 419px; top: 1090px; list-style: none; color: var(--white);
  }
  .contact-list li { display: flex; align-items: center; height: 31px; font-size: 14px; white-space: nowrap; }
  .contact-list li.phone { font-size: 19px; }
  .contact-list svg { margin-right: 8px; flex: none; }
  .contact-divider {
    position: absolute; left: 634px; top: 1088px; width: 1px; height: 100px; background: var(--white);
  }
  .person-name {
    position: absolute; left: 650px; top: 1108px; color: var(--white);
    font-size: 21px; line-height: 23px; font-weight: 400; letter-spacing: .5px; white-space: nowrap;
  }
  .portrait-slot {
    position: absolute; left: 812px; top: 994px; width: 170px; height: 206px;
    background: linear-gradient(180deg, #c99a7e 0%, #b57f68 50%, #c5454e 78%, #b73a45 100%);
    border-radius: 80px 80px 0 0;
  }
</style>
</head>
<body>
<main class="flyer">

  <svg class="hero-art" width="982" height="520" viewBox="0 0 982 520" aria-hidden="true">
    <defs>
      <linearGradient id="leftPhoto" x1="0" y1="0" x2="1" y2="1">
        <stop offset="0" stop-color="#3d8fbd"/>
        <stop offset=".5" stop-color="#5aa9d2"/>
        <stop offset="1" stop-color="#8ecbe6"/>
      </linearGradient>
      <linearGradient id="rightPhoto" x1="0" y1="0" x2="1" y2="1">
        <stop offset="0" stop-color="#5fb8c6"/>
        <stop offset=".6" stop-color="#6cc3c8"/>
        <stop offset="1" stop-color="#4aaebe"/>
      </linearGradient>
      <linearGradient id="bandBlue" x1="0" y1="0" x2="1" y2="0">
        <stop offset="0" stop-color="#0094d4"/>
        <stop offset="1" stop-color="#00a9dd"/>
      </linearGradient>
    </defs>
    <polygon points="0,0 44,0 527,186 432,222 0,55" fill="url(#bandBlue)"/>
    <g role="img" aria-label="Photo of two people shaking hands, tinted blue">
      <polygon points="0,80 585,307 0,580" fill="url(#leftPhoto)"/>
    </g>
    <g role="img" aria-label="Photo of a team stacking hands together, tinted teal">
      <polygon points="444,235 981,14 981,445 585,307" fill="url(#rightPhoto)"/>
    </g>
    <polygon points="150,190 585,307 290,440" fill="#a7e0e2" opacity=".45"/>
    <polyline points="0,106 523,307 0,545" fill="none" stroke="#ffffff" stroke-width="1" opacity=".8"/>
    <polygon points="549,339 614,311 981,455 981,500" fill="url(#bandBlue)"/>
  </svg>

  <svg class="backdrop-fade" width="982" height="420" viewBox="0 0 982 420" aria-hidden="true">
    <defs>
      <linearGradient id="fade" x1="0" y1="0" x2="0" y2="1">
        <stop offset="0" stop-color="#c7ebf8" stop-opacity=".6"/>
        <stop offset="1" stop-color="#e9f6fb" stop-opacity="0"/>
      </linearGradient>
    </defs>
    <polygon points="0,160 520,260 0,420" fill="url(#fade)"/>
    <polygon points="982,205 540,290 982,330" fill="url(#fade)" opacity=".7"/>
  </svg>

  <header class="brand">
    <div class="brand-name">Teodric F. Morvantelk</div>
    <div class="brand-tag">Alternative Dispute Resolution</div>
  </header>

  <h1 class="hero-title">MEDIATION</h1>

  <div class="illustration-slot" role="img" aria-label="Illustration of a raised hand holding a puzzle piece with a light bulb"></div>

  <h2 class="section-head head-what"><span class="accent">WHAT IS</span> <span class="strong">MEDIATION?</span></h2>
  <p class="body-copy copy-one">Mediation is a form of facilitated negotiation, by a mediator, who helps the parties engage in a dialog to search for a joint agreement. All decisions, from agreeing to participate in the mediation, to possible terms of an agreement, are decided by the parties.</p>
  <p class="body-copy copy-two">The mediator has no authority over the parties nor impose any directives. The mediator is there to help the parties find their interests, list and organize the options they have vs the alternatives and the outcome probabilities for each outside a resolution via the mediation process.</p>

  <h2 class="section-head head-services"><span class="accent">SERVICES</span> <span class="strong">OFFERED</span></h2>
  <ul class="services">
    <li>Divorce and Family Mediation</li>
    <li>Commercial and business related Mediation</li>
    <li>International business and trading conflict mediation</li>
    <li>Merger Negotiations &amp; Business Collaboration</li>
    <li>Mediation between dealer, agent, distributor, supplier, and manufacturer</li>
    <li>Contract negotiation consultancy</li>
    <li>Employment contract negotiations</li>
    <li>Mediation for property or entity division</li>
    <li>Workplace Mediation</li>
    <li>Mediation Coaching</li>
    <li>Ombuds contracting</li>
    <li>Mediation via videoconference</li>
    <li>Meetings Facilitation</li>
  </ul>

  <h2 class="section-head head-why"><span class="accent">WHY</span> <span class="strong">MEDIATION?</span></h2>
  <p class="why-intro">There are many advantages to mediation, and below is a list of a few</p>

  <ul class="benefits">
    <li class="benefit">
      <span class="benefit-icon"><svg width="34" height="34" viewBox="0 0 34 34" fill="none" stroke="#0094d4" stroke-width="1.3"><rect x="2" y="4" width="17" height="13" rx="1"/><path d="M6 10l3 3 6-6"/><path d="M6 17v4l4-4"/><circle cx="22" cy="23" r="8"/><path d="M22 18v5l3 2"/><circle cx="28" cy="6" r="4"/></svg></span>
      <span class="benefit-text">Saves parties time and money</span>
    </li>
    <li class="benefit">
      <span class="benefit-icon"><svg width="34" height="34" viewBox="0 0 34 34" fill="none" stroke="#0094d4" stroke-width="1.3"><rect x="5" y="4" width="19" height="26" rx="1"/><path d="M9 11h3M9 17h3M9 23h3M15 11h5"/><path d="M29 8L17 22l-2 5 5-2 12-14z"/></svg></span>
      <span class="benefit-text" style="width:240px">Allows parties to resolve disputes in accordance with own preferences</span>
    </li>
    <li class="benefit">
      <span class="benefit-icon"><svg width="34" height="34" viewBox="0 0 34 34" fill="none" stroke="#0094d4" stroke-width="1.3"><path d="M17 2l12 5v9c0 8-6 13-12 16C11 29 5 24 5 16V7z"/><path d="M17 6l8 3v7c0 5-4 9-8 11-4-2-8-6-8-11V9z"/><path d="M12 16l4 4 7-7"/></svg></span>
      <span class="benefit-text">Confidential, private forum for addressing sensitive issues and exploring settlement</span>
    </li>
    <li class="benefit">
      <span class="benefit-icon"><svg width="34" height="34" viewBox="0 0 34 34" fill="none" stroke="#0094d4" stroke-width="1.3"><circle cx="13" cy="8" r="5"/><path d="M3 27c0-7 4-11 10-11 2 0 4 .5 5 1.5"/><circle cx="24" cy="24" r="7"/><path d="M20.5 24l2.5 2.5 4.5-4.5"/></svg></span>
      <span class="benefit-text">Parties control selection of mediator</span>
    </li>
    <li class="benefit">
      <span class="benefit-icon"><svg width="34" height="34" viewBox="0 0 34 34" fill="none" stroke="#0094d4" stroke-width="1.3"><rect x="2" y="3" width="18" height="13" rx="1"/><path d="M7 10l3 3 5-6"/><path d="M12 16v5h14l4 4V12H20"/></svg></span>
      <span class="benefit-text">Parties retain control over outcome; can end mediation at any time</span>
    </li>
    <li class="benefit">
      <span class="benefit-icon"><svg width="36" height="30" viewBox="0 0 36 30" fill="none" stroke="#0094d4" stroke-width="1.3"><path d="M1 9l6-3 5 10-6 3z"/><path d="M35 9l-6-3-5 10 6 3z"/><path d="M11 15l6 6c1 1 3 1 4 0l6-6"/><path d="M26 8h-7l-5 4 2 2 5-3"/><path d="M10 9l4-1"/></svg></span>
      <span class="benefit-text">Allows for creativity and flexibility in generating options; leads to solutions tailored to meet parties' interests</span>
    </li>
  </ul>

  <div class="rates-bar">SLIDING SCALE RATES AVAILABLE</div>
  <div class="panel-edge"></div>
  <div class="contact-panel"></div>

  <ul class="contact-list">
    <li class="phone"><svg width="18" height="18" viewBox="0 0 24 24" fill="#ffffff"><path d="M6.6 10.8a15 15 0 006.6 6.6l2.2-2.2c.3-.3.7-.4 1-.2 1.1.4 2.3.6 3.6.6.6 0 1 .4 1 1V20c0 .6-.4 1-1 1A17 17 0 013 4c0-.6.4-1 1-1h3.5c.6 0 1 .4 1 1 0 1.3.2 2.5.6 3.6.1.3 0 .7-.2 1z"/></svg>+1.555.384.7290</li>
    <li><svg width="15" height="12" viewBox="0 0 15 12" fill="#ffffff"><path d="M0 0h15v12H0z" opacity=".95"/><path d="M0 0l7.5 6L15 0" fill="none" stroke="#00a9dd" stroke-width="1.4"/></svg>teodric@morvantelkresolve.com</li>
    <li><svg width="15" height="15" viewBox="0 0 16 16" fill="none" stroke="#ffffff" stroke-width="1.2"><circle cx="8" cy="8" r="7"/><ellipse cx="8" cy="8" rx="3" ry="7"/><path d="M1 8h14"/></svg>www.morvantelkresolve.com</li>
  </ul>

  <div class="contact-divider"></div>
  <div class="person-name">TEODRIC<br>MORVANTELK</div>

  <div class="portrait-slot" role="img" aria-label="Portrait photo of the mediator in a red shirt"></div>

</main>
</body>
</html>
```